Elegant Business Cards & Letterhead

We will need the following that need to be designed: Letterhead and Business Cards, there winer will be re-hired for the balance of our stationary needs. Text for the cards and letterheads:

- Corporate Card instead of name
- landline: +971 (4) 362 7041
- mobile: +971 56 2819 605
- 800TUTOR
- email: dubai@velmora-lune.com
- www.velmora-lune.com
- PO Box 387261
Address: Castellan Heights Suite 1708, Dubai UAE

Thank you

Target Market(s)

VIPs, HNWI, High-end Families.

Industry/Entity Type

Luxury Market

Font styles to use
Other font styles liked:
• as explained

Colors

Designer to choose only greyscale colors for use in the design.

Requirements
Must have
• Elegant, Simple, Luxurious, Minimalistic
Nice to have
• Luxury, Golds, Engravings,
Should not have
• Much colors, funky,

```html
<!DOCTYPE html>
<html lang="en">
<head>
<meta charset="utf-8">
<title>Velmora Lune — Letterhead &amp; Business Cards</title>
<link rel="stylesheet" href="https://fonts.googleapis.com/css2?family=Marcellus&family=Figtree:wght@400;500;700&display=swap">
<style>
  :root {
    --backdrop: #939498;
    --paper: #ffffff;
    --ink: #111111;
    --text: #3a3a3a;
    --muted: #555555;
    --band: #231f20;
    --band-inner: #404040;
    --rule: #333333;
  }
  * { margin: 0; padding: 0; box-sizing: border-box; }
  html, body { width: 1200px; height: 1200px; overflow: hidden; }
  body {
    background: var(--backdrop);
    position: relative;
    font-family: "Figtree", "Helvetica Neue", Arial, sans-serif;
    color: var(--ink);
  }
  .icon { width: 1em; height: 1em; fill: currentColor; flex: none; }

  /* Letterhead */
  .letterhead {
    position: absolute; left: 68px; top: 80px;
    width: 735px; height: 1051px;
    background: var(--paper);
  }
  .letterhead .contact-block {
    position: absolute; left: 533px; top: 42px;
    font-size: 14px; color: var(--text); line-height: 21px;
  }
  .contact-block .row { display: flex; align-items: center; gap: 6px; }
  .contact-block .icon { font-size: 12px; color: var(--ink); }

  .brand-mark {
    font-family: "Marcellus", "Times New Roman", serif;
    color: var(--ink); white-space: nowrap;
  }
  .letterhead .brand-mark {
    position: absolute; left: 0; right: 0; top: 152px;
    padding-left: 70px; text-align: center;
    font-size: 55px; line-height: 1;
  }
  .recipient-name {
    position: absolute; left: 48px; top: 254px;
    font-size: 22px; font-weight: 700; letter-spacing: -0.2px;
  }
  .date-label {
    position: absolute; left: 482px; top: 306px;
    font-size: 23px; font-weight: 400;
  }
  .letter-body {
    position: absolute; left: 48px; top: 360px; width: 640px;
    font-size: 12.2px; line-height: 22.9px; letter-spacing: 0.85px;
    color: var(--text); text-align: justify;
  }
  .letter-body p + p { margin-top: 10px; }
  .signature {
    position: absolute; left: 60px; top: 891px; width: 133px;
    border-top: 1.5px solid var(--rule);
    text-align: center; font-size: 14px; padding-top: 8px;
  }
  .footer-contact {
    position: absolute; top: 949px; font-size: 14px; color: var(--text);
    display: flex; align-items: center; gap: 7px;
  }
  .footer-contact .icon { font-size: 11px; color: var(--ink); }
  .footer-contact.email { left: 48px; }
  .footer-contact.web { right: 47px; }
  .footer-band {
    position: absolute; left: 0; bottom: 0; width: 735px; height: 71px;
    background: var(--band);
  }
  .footer-band svg.shape { position: absolute; left: 0; top: 0; }
  .footer-band .address {
    position: absolute; left: 0; right: 0; top: 8px;
    display: flex; justify-content: center; align-items: center; gap: 8px;
    color: #ffffff; font-size: 14px;
  }
  .footer-band .address .icon { font-size: 15px; }

  /* Business cards */
  .card { position: absolute; left: 846px; width: 285px; height: 183px; }
  .card-front { top: 416px; background: var(--paper); }
  .card-back { top: 612px; background: var(--band); color: #ffffff; }
  .card-front .brand-mark {
    position: absolute; left: 19px; top: 83px; font-size: 15.5px; line-height: 1;
  }
  .card-front .divider {
    position: absolute; left: 150px; top: 43px; width: 1px; height: 97px;
    background: var(--rule);
  }
  .card-front .details { position: absolute; left: 164px; top: 41px; }
  .card-front .name { font-size: 13px; font-weight: 700; line-height: 16px; }
  .card-front .title { font-size: 7.8px; color: var(--muted); margin-top: 2px; }
  .card-front .lines { margin-top: 8px; font-size: 8px; color: var(--text); line-height: 13px; }
  .card-front .lines .row { display: flex; align-items: center; gap: 4px; }
  .card-front .lines .icon { font-size: 6.5px; color: var(--ink); }
  .card-front .address {
    position: absolute; left: 0; right: 0; top: 158px;
    text-align: center; font-size: 7.6px; color: var(--text);
  }
  .card-back .brand-mark {
    position: absolute; left: 0; right: 0; top: 75px;
    text-align: center; font-size: 28.5px; line-height: 1; color: #ffffff;
  }
  .card-back .hotline {
    position: absolute; left: 0; right: 0; top: 149px;
    text-align: center; font-size: 8.3px; font-weight: 700;
  }
</style>
</head>
<body>

<svg width="0" height="0" style="position:absolute" aria-hidden="true">
  <defs>
    <symbol id="i-phone" viewBox="0 0 24 24"><path d="M6.6 10.8a15.1 15.1 0 0 0 6.6 6.6l2.2-2.2a1 1 0 0 1 1-.25 11.4 11.4 0 0 0 3.6.57 1 1 0 0 1 1 1V20a1 1 0 0 1-1 1A17 17 0 0 1 3 4a1 1 0 0 1 1-1h3.5a1 1 0 0 1 1 1c0 1.25.2 2.45.57 3.57a1 1 0 0 1-.25 1z"/><path d="M14 3a7 7 0 0 1 7 7h-2a5 5 0 0 0-5-5zm0 4a3 3 0 0 1 3 3h-2a1 1 0 0 0-1-1z"/></symbol>
    <symbol id="i-mobile" viewBox="0 0 24 24"><path d="M7 1h10a2 2 0 0 1 2 2v18a2 2 0 0 1-2 2H7a2 2 0 0 1-2-2V3a2 2 0 0 1 2-2zm0 3v14h10V4zm5 15.5a1.2 1.2 0 1 0 0 2.4 1.2 1.2 0 0 0 0-2.4z"/></symbol>
    <symbol id="i-fax" viewBox="0 0 24 24"><path d="M6 2h9l3 3v4H6zM4 10h16a2 2 0 0 1 2 2v6h-4v4H6v-4H2v-6a2 2 0 0 1 2-2zm4 6v4h8v-4z"/></symbol>
    <symbol id="i-mail" viewBox="0 0 24 24"><path d="M2 4h20v16H2zm2 2.5V18h16V6.5l-8 6z"/><path d="M4 4h16l-8 6z"/></symbol>
    <symbol id="i-globe" viewBox="0 0 24 24"><path d="M12 1a11 11 0 1 0 0 22 11 11 0 0 0 0-22zm7.9 10h-3.5a16 16 0 0 0-1.5-6.9A9 9 0 0 1 19.9 11zM12 3.1c1 1.3 2.2 4 2.4 7.9H9.6c.2-3.9 1.4-6.6 2.4-7.9zM9.1 4.1A16 16 0 0 0 7.6 11H4.1a9 9 0 0 1 5-6.9zM4.1 13h3.5a16 16 0 0 0 1.5 6.9 9 9 0 0 1-5-6.9zm7.9 7.9c-1-1.3-2.2-4-2.4-7.9h4.8c-.2 3.9-1.4 6.6-2.4 7.9zm2.9-1a16 16 0 0 0 1.5-6.9h3.5a9 9 0 0 1-5 6.9z"/></symbol>
    <symbol id="i-pin" viewBox="0 0 24 24"><path d="M12 1a8 8 0 0 0-8 8c0 6 8 14 8 14s8-8 8-14a8 8 0 0 0-8-8zm0 11a3 3 0 1 1 0-6 3 3 0 0 1 0 6z"/></symbol>
  </defs>
</svg>

<section class="letterhead">
  <div class="contact-block">
    <div class="row"><svg class="icon"><use href="#i-phone"/></svg>+971 (4) 362 7041</div>
    <div class="row"><svg class="icon"><use href="#i-mobile"/></svg>+971 56 2819 605</div>
    <div class="row"><svg class="icon"><use href="#i-fax"/></svg>+971 (4) 362 7049</div>
  </div>

  <div class="brand-mark">VELMORA LUNE</div>

  <h1 class="recipient-name">Adrian Calloway</h1>
  <div class="date-label">Date:</div>

  <div class="letter-body">
    <p>Lorem Ipsum is simply dummy text of the printing and typesetting industry. Lorem Ipsum has been the industry's standard dummy text ever since the 1500s, when an unknown printer took a galley of type and scrambled it to make a type specimen book. It has survived not only five centuries, but also the leap into electronic typesetting, remaining essentially unchanged. It was popularised in the 1960s with the release of Typeline sheets containing Lorem Ipsum passages, and more recently with desktop publishing software like Folio Press including versions of Lorem Ipsum.</p>
    <p>It is a long established fact that a reader will be distracted by the readable content of a page when looking at its layout. The point of using Lorem Ipsum is that it has a more-or-less normal distribution of letters, as opposed to using 'Content here, content here', making it look like readable English. Many desktop publishing packages and web page editors now use Lorem Ipsum as their default model text, and a search for 'lorem ipsum' will uncover many web sites still in their infancy. Various versions have evolved over the years, sometimes by accident, sometimes on purpose (injected humour and the like).</p>
    <p>Contrary to popular belief, Lorem Ipsum is not simply random text. It has roots in a piece of classical Latin literature from 45 BC, making it over 2000 years old. Henry Marlowe, a Latin professor at Ashford-Wells College in Virginia, looked up one of the more obscure Latin words, consectetur, from a Lorem Ipsum passage, and going through the cites of the word in classical literature, discovered the undoubtable source. Lorem Ipsum comes from sections 1.10.32 and 1.10.33 of "de Finibus Bonorum et Malorum" (The Extremes of Good and Evil) by Cicero, written in 45 BC. This book is a treatise on the theory of ethics, very popular during the Renaissance. The first line of Lorem Ipsum, "Lorem ipsum dolor sit amet..", comes from a line in section 1.10.32.</p>
  </div>

  <div class="signature">Signeture</div>

  <div class="footer-contact email"><svg class="icon"><use href="#i-mail"/></svg>dubai@velmora-lune.com</div>
  <div class="footer-contact web"><svg class="icon"><use href="#i-globe"/></svg>www.velmora-lune.com</div>

  <div class="footer-band">
    <svg class="shape" width="735" height="71" viewBox="0 0 735 71" aria-hidden="true">
      <polygon points="84,0 650,0 607,48 127,48" fill="#ffffff"/>
      <polygon points="98,0 636,0 605,37 129,37" fill="var(--band-inner)"/>
    </svg>
    <div class="address"><svg class="icon"><use href="#i-pin"/></svg>PO Box 387261 Castellan Heights Suite 1708, Dubai UAE</div>
  </div>
</section>

<section class="card card-front">
  <div class="brand-mark">VELMORA LUNE</div>
  <div class="divider"></div>
  <div class="details">
    <div class="name">Adrian Calloway</div>
    <div class="title">Founder &amp; Director</div>
    <div class="lines">
      <div class="row"><svg class="icon"><use href="#i-phone"/></svg>+971 (4) 362 7041</div>
      <div class="row"><svg class="icon"><use href="#i-mobile"/></svg>+971 56 2819 605</div>
      <div class="row"><svg class="icon"><use href="#i-fax"/></svg>+971 (4) 362 7049</div>
      <div class="row"><svg class="icon"><use href="#i-mail"/></svg>dubai@velmora-lune.com</div>
      <div class="row"><svg class="icon"><use href="#i-globe"/></svg>www.velmora-lune.com</div>
    </div>
  </div>
  <div class="address">PO Box 387261 Castellan Heights Suite 1708, Dubai UAE</div>
</section>

<section class="card card-back">
  <div class="brand-mark">VELMORA LUNE</div>
  <div class="hotline">Call Us: 800TUTOR</div>
</section>

</body>
</html>
```